2015 Conference Header

I would like a header designed for our conference next year. It will be used on all of our event promotional material. The information and images that can be used are in the drop box file. I have also included examples of what we have used in the past.

https://www.filecrate.example/sh/7x2k9qpl4mzr8t/QWtyR834kdLmPnBv2ZsXcUoRe?dl=0

Industry/Entity Type

Event

Requirements
Must have
• To give you all a little more idea on our branding colours and designs our business website is www.brightvanecasting.example

```html
<!DOCTYPE html>
<html lang="en">
<head>
<meta charset="utf-8">
<title>Spincast 2015 Conference Header</title>
<link rel="stylesheet" href="https://fonts.googleapis.com/css2?family=Montserrat:wght@600&family=Questrial&display=swap">
<style>
  :root {
    --page-bg: #e8ecf0;
    --photo-sky: #9fb3c4;
    --photo-city: #8c8172;
    --photo-green: #5f6e4e;
    --bronze: #b07a3a;
    --bronze-dark: #8a5a2b;
    --panel-light: #f6f6f6;
    --panel-shade: #d6d6d6;
    --ink: #4a4a4a;
    --banner-edge: #2b2b2b;
  }
  * { margin: 0; padding: 0; box-sizing: border-box; }
  html, body {
    width: 1200px;
    height: 900px;
    overflow: hidden;
    background: var(--page-bg);
  }
  .canvas {
    position: relative;
    width: 1200px;
    height: 900px;
  }
  .header-banner {
    position: absolute;
    left: 50px;
    top: 182px;
    width: 1100px;
    height: 536px;
    border-radius: 28px;
    overflow: hidden;
    box-shadow: 0 0 0 4px var(--banner-edge);
  }
  .city-photo {
    position: absolute;
    left: 0;
    top: 0;
    width: 680px;
    height: 536px;
    background:
      linear-gradient(180deg, var(--photo-sky) 0%, var(--photo-city) 35%, var(--photo-city) 65%, var(--photo-green) 100%);
  }
  .info-panel-shape {
    position: absolute;
    inset: 0;
    width: 1100px;
    height: 536px;
  }
  .event-info {
    position: absolute;
    left: 630px;
    top: 0;
    width: 440px;
    height: 536px;
    text-align: center;
    font-family: "Questrial", sans-serif;
    color: var(--ink);
  }
  .event-title {
    position: absolute;
    top: 112px;
    width: 100%;
    font-family: "Montserrat", sans-serif;
    font-weight: 600;
    font-size: 50px;
    letter-spacing: 2px;
    color: var(--bronze-dark);
  }
  .event-year {
    position: absolute;
    top: 182px;
    width: 100%;
    font-size: 50px;
  }
  .event-place {
    position: absolute;
    top: 296px;
    width: 100%;
    font-size: 36px;
  }
  .event-dates {
    position: absolute;
    top: 346px;
    width: 100%;
    font-size: 36px;
  }
  .event-rule {
    position: absolute;
    top: 432px;
    left: -10px;
    width: 460px;
    height: 2px;
    background: var(--bronze);
  }
  .event-web {
    position: absolute;
    top: 446px;
    width: 100%;
    font-size: 22px;
  }
</style>
</head>
<body>
<main class="canvas">
  <section class="header-banner">
    <div class="city-photo" role="img" aria-label="Aerial photograph of the Adelaide city centre with the river, parklands and stadium"></div>
    <svg class="info-panel-shape" viewBox="0 0 1100 536" aria-hidden="true">
      <defs>
        <linearGradient id="panelFill" x1="0" y1="0" x2="0" y2="1">
          <stop offset="0" stop-color="var(--panel-light)"/>
          <stop offset="1" stop-color="var(--panel-shade)"/>
        </linearGradient>
      </defs>
      <path class="bronze-band" transform="translate(-24 0)" fill="var(--bronze)"
            d="M625 0 C612 50 615 100 640 140 L672 160 L640 180 C612 230 598 330 600 536 L1124 536 L1124 0 Z"/>
      <path class="panel-fill" fill="url(#panelFill)"
            d="M625 0 C612 50 615 100 640 140 L672 160 L640 180 C612 230 598 330 600 536 L1100 536 L1100 0 Z"/>
    </svg>
    <div class="event-info">
      <h1 class="event-title">SPINCAST</h1>
      <p class="event-year">2015</p>
      <p class="event-place">Adelaide, Australia</p>
      <p class="event-dates">21 - 23 June</p>
      <div class="event-rule"></div>
      <p class="event-web">www.spincastconference.example</p>
    </div>
  </section>
</main>
</body>
</html>
```